Flyer-Design für Fusspflege für den Mann
schade dass die Daten nicht auch im psd-format geliefert werden konnten
Zielgruppe
Fusspflege und Maniküre für den Mann - neu und zusammen in einem Haarentfernungsinstitut für Männer in Zürich
Aufgabenstellung
Sie haben freie Wahl - Farben an das Logo angepasst.
Für tolle Bilder bin ich offen.
Sollte auch stehen: nur auf Voranmeldung - am besten per SMS
Zudem das persönliche Foto dazu

```html
<!DOCTYPE html>
<html lang="de">
<head>
<meta charset="utf-8">
<title>Fusspflege für den Mann – Flyer 140x140 mm</title>
<link rel="stylesheet" href="https://fonts.googleapis.com/css2?family=Fira+Sans:wght@400&family=Open+Sans:wght@400;600;700&family=Libre+Caslon+Text&display=swap">
<style>
  :root {
    --brown: #7c6754;
    --gold: #d8bc84;
    --white: #ffffff;
    --ink: #1f1f1f;
    --text-grey: #6e6259;
    --toe-tone-a: #ffffff;
    --toe-tone-b: #f1ece6;
    --photo-a: #d9c6b6;
    --photo-b: #8c5e5e;
  }
  * { margin: 0; padding: 0; box-sizing: border-box; }
  html, body { width: 1200px; height: 1183px; overflow: hidden; background: var(--white); }
  .sheet { position: relative; width: 1200px; height: 1183px; }
  .format-label {
    position: absolute; top: 88px; left: 0; width: 1158px; text-align: center;
    font-family: "Libre Caslon Text", serif; font-size: 26px; color: var(--ink);
  }
  .flyer {
    position: absolute; left: 139px; top: 179px; width: 852px; height: 854px;
    background: var(--brown);
    box-shadow: 18px 20px 12px rgba(60, 60, 60, 0.75);
    overflow: hidden;
  }
  .flyer-shapes { position: absolute; inset: 0; }
  .headline {
    position: absolute; top: 44px; right: 55px; text-align: right;
    font-family: "Fira Sans", sans-serif; font-weight: 400; font-size: 27px;
    line-height: 39px; color: var(--white); letter-spacing: 0.4px;
  }
  .brand {
    position: absolute; left: 140px; top: 500px; width: 170px; text-align: center;
  }
  .brand-dot {
    display: block; width: 56px; height: 56px; margin: 0 auto 70px;
    border-radius: 50%; background: var(--gold);
  }
  .brand-name {
    font-family: "Open Sans", sans-serif; font-weight: 600; font-size: 34px;
    color: var(--brown); white-space: nowrap;
  }
  .info { position: absolute; left: 353px; top: 548px; color: var(--brown); font-family: "Open Sans", sans-serif; }
  .booking { font-weight: 700; font-size: 18px; color: var(--gold); line-height: 24px; }
  .service { margin-top: 12px; font-weight: 700; font-size: 28px; line-height: 43px; }
  .contact { margin-top: 22px; display: flex; font-size: 20px; line-height: 28.5px; color: var(--text-grey); }
  .contact-address { width: 283px; font-style: normal; }
  .contact-company { font-weight: 700; font-size: 19px; color: var(--brown); }
  .contact-online { padding-top: 28.5px; }
</style>
</head>
<body>
<div class="sheet">
  <p class="format-label">Format 140x140 mm</p>

  <section class="flyer">
    <svg class="flyer-shapes" width="852" height="854" viewBox="0 0 852 854">
      <defs>
        <linearGradient id="portraitTone" x1="0" y1="0" x2="1" y2="1">
          <stop offset="0" stop-color="var(--photo-a)"/>
          <stop offset="1" stop-color="var(--photo-b)"/>
        </linearGradient>
        <linearGradient id="toeTone" x1="0" y1="0" x2="1" y2="1">
          <stop offset="0" stop-color="var(--toe-tone-a)"/>
          <stop offset="1" stop-color="var(--toe-tone-b)"/>
        </linearGradient>
      </defs>
      <polygon class="portrait" role="img" aria-label="Porträtfoto des Inhabers"
        points="26,191 55,151 108,95 148,78 195,77 235,81 269,105 298,168 320,251 301,288 261,308 221,335 175,368 141,355 108,315 71,261 35,221"
        fill="url(#portraitTone)" stroke="var(--white)" stroke-width="1.5"/>
      <g class="footprint-area" role="img" aria-label="Grosse Fussabdruck-Illustration in Weiss">
        <rect class="footprint-toes" x="345" y="150" width="507" height="240" rx="40" fill="url(#toeTone)"/>
        <rect class="footprint-sole" x="75" y="425" width="820" height="480" rx="110" fill="var(--white)"/>
      </g>
    </svg>

    <h1 class="headline">Auch Männer müssen auf ihr<br>Erscheinungsbild achten!</h1>

    <div class="brand">
      <span class="brand-dot"></span>
      <p class="brand-name">FussWerk</p>
    </div>

    <div class="info">
      <p class="booking">Nur auf Voranmeldung!</p>
      <h2 class="service">Verwöhnende Pediküre &amp;<br>Maniküre für den Mann</h2>
      <div class="contact">
        <address class="contact-address">
          <span class="contact-company">FussWerk by GlattHaut</span><br>
          Marco Brunner<br>
          Lindenweg 14<br>
          CH - 8005 Zürich
        </address>
        <p class="contact-online">
          www.glatthaut.ch<br>
          marco@glatthaut.ch<br>
          079 312 45 67
        </p>
      </div>
    </div>
  </section>
</div>
</body>
</html>
```